New business logo / Business Card Design

My company provides Interim Management and consultancy, for Facilities Services. Covers any aspect of facilities management, including M&E, helpdesk, asset management, supplier relationships, catering, cleaning etc. Company provides innovative solutions to exceed client needs, drawing on years of experience. Initial thoughts on logo are attached below. Fits with RAG status on projects, red, amber and green, with logo design colours around moving services from amber to green.

Target Market(s)

Facilities Management clients and service providers

Industry/Entity Type

Business

Contact Information for Business Card

Company Name = k7Rventures Ltd My name on card = Derek Whitcombe, Director Mobile = 07516309842 Email = Derek@k7rventuresltd.co.uk Twitter = @k7Rventures Ltd

Font styles to use
Sans Serif

Colors
f37122
00a990

Requirements
Must have
• Logo to be evident, with some background image in reference to Facilities Management

```html
<!DOCTYPE html>
<html lang="en">
<head>
<meta charset="utf-8">
<title>k7Rventures Ltd — Business Card</title>
<link href="https://fonts.googleapis.com/css2?family=Roboto:wght@400;500;900&display=swap" rel="stylesheet">
<style>
  :root {
    --page-bg: #ddd7cd;
    --card-light: #f1f1ef;
    --card-mid: #e3e2df;
    --card-dark: #0b0b0b;
    --ink: #222222;
    --accent-orange: #d9541e;
    --accent-green: #2e6a48;
  }
  html, body {
    margin: 0;
    padding: 0;
    width: 1200px;
    height: 970px;
    overflow: hidden;
    background: var(--page-bg);
    font-family: "Roboto", Arial, sans-serif;
  }
  .canvas {
    position: relative;
    width: 1200px;
    height: 970px;
  }
  .card {
    position: absolute;
    left: 100px;
    top: 157px;
    width: 1000px;
    height: 655px;
    overflow: hidden;
    background: linear-gradient(160deg, var(--card-light) 0%, var(--card-mid) 60%, #e9dcdc 100%);
    box-shadow: 0 10px 30px rgba(0,0,0,0.18);
  }
  .card-art {
    position: absolute;
    inset: 0;
    width: 100%;
    height: 100%;
  }
  .company-name {
    position: absolute;
    left: 60px;
    top: 108px;
    margin: 0;
    font-size: 62px;
    font-weight: 900;
    letter-spacing: 0.5px;
    color: var(--ink);
    line-height: 1;
  }
  .person {
    position: absolute;
    left: 56px;
    top: 336px;
  }
  .person-name {
    margin: 0;
    font-size: 44px;
    font-weight: 500;
    color: var(--ink);
    line-height: 1;
  }
  .person-role {
    margin: 2px 0 0;
    font-size: 34px;
    font-weight: 400;
    color: var(--accent-orange);
    line-height: 1;
  }
  .contacts {
    position: absolute;
    left: 56px;
    top: 463px;
    margin: 0;
    padding: 0;
    list-style: none;
  }
  .contact-item {
    display: flex;
    align-items: center;
    height: 37px;
    font-size: 30px;
    color: var(--ink);
  }
  .contact-icon {
    width: 30px;
    height: 30px;
    margin-right: 14px;
    flex: none;
  }
</style>
</head>
<body>
<main class="canvas">
  <section class="card" aria-label="Business card">
    <svg class="card-art" viewBox="0 0 1000 655" preserveAspectRatio="none" aria-hidden="true">
      <path d="M700 0 C 870 60, 965 200, 908 330 C 862 470, 720 600, 611 655 L1000 655 L1000 0 Z" fill="var(--card-dark)"/>
      <path d="M672 0 C 860 70, 938 200, 896 330 C 842 480, 560 620, 340 655" fill="none" stroke="var(--accent-orange)" stroke-width="7"/>
    </svg>

    <h1 class="company-name">k7Rventures Ltd</h1>

    <div class="person">
      <p class="person-name">Derek Whitcombe</p>
      <p class="person-role">Director</p>
    </div>

    <ul class="contacts">
      <li class="contact-item">
        <svg class="contact-icon" viewBox="0 0 30 30" aria-hidden="true">
          <rect width="30" height="30" fill="var(--accent-green)"/>
          <rect x="9" y="4" width="12" height="22" rx="2" fill="none" stroke="#fff" stroke-width="2"/>
          <rect x="11.5" y="7" width="7" height="8" fill="#fff"/>
        </svg>
        07516309842
      </li>
      <li class="contact-item">
        <svg class="contact-icon" viewBox="0 0 30 30" aria-hidden="true">
          <rect width="30" height="30" fill="var(--accent-green)"/>
          <rect x="5" y="8" width="20" height="14" fill="none" stroke="#fff" stroke-width="2"/>
          <path d="M5 8 L15 16 L25 8 M5 22 L12 14 M25 22 L18 14" fill="none" stroke="#fff" stroke-width="1.6"/>
        </svg>
        Derek@k7rventuresltd.co.uk
      </li>
      <li class="contact-item">
        <svg class="contact-icon" viewBox="0 0 30 30" aria-hidden="true">
          <rect width="30" height="30" fill="var(--accent-green)"/>
        </svg>
        @k7Rventures Ltd
      </li>
    </ul>
  </section>
</main>
</body>
</html>
```